Technology solutions catalog

Were looking for a catalogue to supplement our website and corporate branding.

Our website will give you a good understanding of our products and services as well as our theme.

Our base colour and logo is red, white and grey.

www.voltrane.com.au

The aim of the catalogue is to showcase our business IT services & solutions. This will be a mix of education about the new solutions available to small and medium business today and how these solutions can increase productivity.

We would also like tip sections

This isn't all about selling but also about educating SMB's of the new and exciting IT solutions available today and having them book a free consult with us to discuss further about how we can help the business.

Solutions and area's that the catalogue will need to cover include

Front Cover -
-About us section, with our business contact information (1st page)
- Introduction. (2nd page)
-Communication Solutions - this includes Email, IP phones and business IT networks (2 pages)
- Data & Storage solutions (2 pages)
- Hardware (1 pages)
- Business IT health check list (1 page)
- Services and support offering (2 pages)
- Software & Popular cloud solutions (2 pages)
- Website / E-commerce solutions (2 pages)
Back cover

Based on two pages per solution the whole catalogue will be around 14 pages.

We don't need any text content done. We would like Headings on pages including page numbers. Footer please.

We're looking for a template that we can have our designer finish off by adding in some further product and service image and text.

Thank you for your consideration

Target Market(s)

IT for small and medium businesses

Industry/Entity Type

Supplement

Requirements
Must have
• Size A4
• Design supplied in Adobe indesign so we can edit and add our text and content
• Clean design

```html
<!DOCTYPE html>
<html lang="en">
<head>
<meta charset="utf-8">
<title>Voltrane Catalogue Covers</title>
<link rel="stylesheet" href="https://fonts.googleapis.com/css2?family=Open+Sans:wght@400;700;800&display=swap">
<style>
  :root {
    --stage: #e6e6e6;
    --red-deep: #9c1a22;
    --red: #c0272f;
    --red-soft: #cf4b53;
    --white: #ffffff;
    --paper: #f4f4f4;
    --map-grey: #e2e3e5;
    --sky-deep: #0f4f86;
    --sky: #3f8fcf;
    --sky-light: #a9d3ef;
  }
  html, body {
    margin: 0;
    width: 1200px;
    height: 849px;
    overflow: hidden;
    background: var(--stage);
    font-family: "Open Sans", Arial, sans-serif;
  }
  .spread {
    position: relative;
    width: 1200px;
    height: 849px;
  }
  .cover {
    position: absolute;
    top: 240px;
    width: 530px;
    height: 372px;
    box-shadow: 0 10px 24px rgba(0,0,0,0.18);
    overflow: hidden;
  }
  /* back cover */
  .back-cover {
    left: 50px;
    background: linear-gradient(115deg, var(--red-deep) 0%, var(--red) 45%, var(--red-soft) 100%);
    color: var(--white);
  }
  .back-cover .brand-name {
    position: absolute;
    left: 40px;
    top: 26px;
    margin: 0;
    font-size: 30px;
    font-weight: 800;
    letter-spacing: 0.2px;
    color: var(--white);
  }
  .contact-block {
    position: absolute;
    right: 40px;
    top: 236px;
    text-align: right;
    font-size: 8px;
    line-height: 1.35;
    font-weight: 400;
  }
  .contact-block .address { margin: 0 0 6px; font-style: normal; }
  .contact-block .label { display: block; }
  .web-links {
    position: absolute;
    left: 0;
    right: 0;
    top: 330px;
    text-align: center;
    font-size: 9px;
    font-weight: 700;
    margin: 0;
  }
  /* front cover */
  .front-cover {
    left: 620px;
    background: var(--paper);
  }
  .map-area {
    position: absolute;
    left: 0; top: 0;
    width: 100%;
    height: 130px;
    background: radial-gradient(ellipse at 55% 40%, var(--map-grey) 0%, var(--paper) 75%);
  }
  .front-cover .brand-name {
    position: absolute;
    right: 28px;
    top: 78px;
    margin: 0;
    font-size: 33px;
    font-weight: 800;
    color: var(--red);
  }
  .city-photo {
    position: absolute;
    left: 0;
    top: 134px;
    width: 100%;
    height: 238px;
    background: linear-gradient(120deg, var(--sky-deep) 0%, var(--sky) 40%, var(--sky-light) 55%, var(--sky) 70%, var(--sky-deep) 100%);
  }
</style>
</head>
<body>
<main class="spread">
  <section class="cover back-cover" aria-label="Back cover">
    <h2 class="brand-name">Voltrane</h2>
    <div class="contact-block">
      <address class="address">
        <span class="label">ADDRESS 01</span>
        Nordlicht Büro, Lindenweg 42<br>
        10115 Berlin, Germany<br>
        Telephone: +49 30 5550 1234
      </address>
      <address class="address">
        <span class="label">ADDRESS 02</span>
        Nordlicht Büro, Lindenweg 42<br>
        10115 Berlin, Germany<br>
        Telephone: +49 30 5550 1234
      </address>
    </div>
    <p class="web-links">www.voltrane.com.au | facebook/voltrane.com.au</p>
  </section>

  <section class="cover front-cover" aria-label="Front cover">
    <div class="map-area" role="img" aria-label="Faint world map in light grey"></div>
    <h1 class="brand-name">Voltrane</h1>
    <div class="city-photo" role="img" aria-label="Photo of glass office towers and a passing airplane under a bright blue sky with floating data graphics"></div>
  </section>
</main>
</body>
</html>
```